M Website

We need a website design for a construction plant company. You may use a combination of our photos and the stock images. See the logo for company colours. It also be of great value to see moving pictures like the ones on the link: https://www.bellwickventures.co.za/copy-of-about-us. See our uploaded files for content.

Target Market(s)

Construction

Number of Pages Required

5+ page

```html
<!DOCTYPE html>
<html lang="en">
<head>
<meta charset="utf-8">
<title>Key Fields</title>
<link href="https://fonts.googleapis.com/css2?family=Roboto:wght@400;700&family=Roboto+Condensed:wght@700&display=swap" rel="stylesheet">
<style>
  :root {
    --bg: #ffffff;
    --ink: #1f1f1f;
    --body: #3a3a3a;
    --accent: #f2b01e;
    --numeral: #fbeacf;
  }
  * { margin: 0; padding: 0; box-sizing: border-box; }
  html, body { width: 718px; height: 1200px; overflow: hidden; background: var(--bg); }
  .canvas { position: relative; width: 718px; height: 1200px; font-family: "Roboto", sans-serif; }

  .section-title {
    position: absolute; top: 28px; left: 0; width: 718px; text-align: center;
    font-family: "Roboto Condensed", sans-serif; font-weight: 700; font-size: 17px;
    color: var(--ink); letter-spacing: 0.2px;
  }
  .section-title .label { position: relative; display: inline-block; padding: 4px 6px; }
  .section-title svg { position: absolute; width: 8px; height: 8px; }
  .section-title .corner-tl { top: 0; left: 0; }
  .section-title .corner-br { bottom: -1px; right: -1px; }

  .photo { position: absolute; }
  .photo-roller { left: 40px; top: 100px; width: 315px; height: 210px;
    background: linear-gradient(180deg, #8fb4d6 0%, #6d8a4e 35%, #c9a235 60%, #cfcac0 100%); }
  .photo-pipeline { left: 363px; top: 381px; width: 315px; height: 210px;
    background: linear-gradient(180deg, #b7c8dc 0%, #5f6f3a 35%, #3e4a2a 70%, #7c7f86 100%); }
  .photo-loaders { left: 42px; top: 661px; width: 313px; height: 203px;
    background: linear-gradient(180deg, #6f7fa0 0%, #d3a92a 40%, #2c2c2c 72%, #b7b0a4 100%); }
  .photo-site { left: 363px; top: 940px; width: 315px; height: 210px;
    background: linear-gradient(160deg, #4b4f55 0%, #b9b3aa 45%, #c26a4a 60%, #d8d2c6 100%); }

  .field { position: absolute; width: 290px; }
  .field-numeral {
    position: absolute; left: 0; top: -38px;
    font-family: "Roboto", sans-serif; font-weight: 700; font-size: 150px; line-height: 1;
    color: var(--numeral); z-index: 0;
  }
  .field-heading {
    position: relative; z-index: 1;
    font-size: 8.5px; font-weight: 700; letter-spacing: 2.2px; text-transform: uppercase;
    color: var(--ink);
  }
  .field-heading .bracket { color: var(--accent); font-weight: 400; font-size: 11px; letter-spacing: 0; }
  .field-heading .bracket-open { margin-right: 5px; }
  .field-heading .bracket-close { margin-left: 3px; }
  .field-text {
    position: relative; z-index: 1; margin: 30px 0 0 9px;
    font-size: 11.6px; line-height: 21px; color: var(--body); letter-spacing: 0.15px;
  }

  .field-roads { left: 405px; top: 140px; }
  .field-roads .field-numeral { left: 6px; top: -24px; }
  .field-water { left: 45px; top: 418px; }
  .field-water .field-numeral { left: 6px; top: -36px; }
  .field-sanitation { left: 405px; top: 700px; }
  .field-sanitation .field-numeral { left: -2px; top: -42px; }
  .field-housing { left: 45px; top: 979px; }
  .field-housing .field-numeral { left: 6px; top: -40px; }
</style>
</head>
<body>
<div class="canvas">
  <h2 class="section-title">
    <span class="label">
      <svg class="corner-tl" viewBox="0 0 8 8"><path d="M1 8V1h7" fill="none" stroke="#f2b01e" stroke-width="2"/></svg>
      KEY FIELDS
      <svg class="corner-br" viewBox="0 0 8 8"><path d="M0 7h7V0" fill="none" stroke="#f2b01e" stroke-width="2"/></svg>
    </span>
  </h2>

  <div class="photo photo-roller" role="img" aria-label="Yellow road roller compacting a road among palm trees"></div>
  <div class="field field-roads">
    <span class="field-numeral">1</span>
    <h3 class="field-heading"><span class="bracket bracket-open">[</span>Roads and Stormwater<span class="bracket bracket-close">]</span></h3>
    <p class="field-text">Areas of road construction include seal extensions, Area Wide Pavement Treatments and new road formations for Local Authorities, developers, farmers and forestry companies.</p>
  </div>

  <div class="field field-water">
    <span class="field-numeral">2</span>
    <h3 class="field-heading"><span class="bracket bracket-open">[</span>Water Infrastructure<span class="bracket bracket-close">]</span></h3>
    <p class="field-text">Areas of road construction include seal extensions, Area Wide Pavement Treatments and new road formations for Local Authorities, developers, farmers and forestry companies.</p>
  </div>
  <div class="photo photo-pipeline" role="img" aria-label="Pipeline running down a wooded hillside toward a valley"></div>

  <div class="photo photo-loaders" role="img" aria-label="Two yellow backhoe loaders on a construction site"></div>
  <div class="field field-sanitation">
    <span class="field-numeral">3</span>
    <h3 class="field-heading"><span class="bracket bracket-open">[</span>Sanitation Infrastructure<span class="bracket bracket-close">]</span></h3>
    <p class="field-text">Areas of road construction include seal extensions, Area Wide Pavement Treatments and new road formations for Local Authorities, developers, farmers and forestry companies.</p>
  </div>

  <div class="field field-housing">
    <span class="field-numeral">4</span>
    <h3 class="field-heading"><span class="bracket bracket-open">[</span>Hausing<span class="bracket bracket-close">]</span></h3>
    <p class="field-text">Areas of road construction include seal extensions, Area Wide Pavement Treatments and new road formations for Local Authorities, developers, farmers and forestry companies.</p>
  </div>
  <div class="photo photo-site" role="img" aria-label="Workers stacking bricks and cement bags on a building site"></div>
</div>
</body>
</html>
```